RV Park - Advertising RV Park using Billboard 12 ft wide by 6 ft tall size

We need a sign for a relatively new RV Park called Bramblewood of Carver RV Park at 2745 Danbury Road, Ashford Hollow , NC. The sign should include our web address and phone number. bramblewoodcarverrv.example, 555-314-2967. We would like to see designs that include nice color and no tacky cartoons. Final design should communicate a nice and safe RV Park. We would also like to include quick directions - Just Ahead! Left on Kestrel Rd then left on Danbury Rd. (A nice motor home or RV representation may be nice but not mandatory to be included.) Classic but eye catching design. Sign is 12 ft wide by 6 ft tall in size. Will likely be vinyl printed.

```html
<!DOCTYPE html>
<html lang="en">
<head>
<meta charset="utf-8">
<title>Bramblewood of Carver RV Park – Billboard</title>
<link rel="stylesheet" href="https://fonts.googleapis.com/css2?family=Montserrat:wght@900&family=Archivo+Narrow:wght@700&family=Krona+One&family=Rubik:wght@600&family=Poppins:wght@300;600&display=swap">
<style>
  :root {
    --paper: #ffffff;
    --ink: #111111;
    --brand-red: #7a1410;
    --brand-red-deep: #560b08;
    --brand-red-light: #93201a;
    --pin-red: #e4161b;
    --stage: #f4f4f4;
  }
  * { margin: 0; padding: 0; box-sizing: border-box; }
  html, body { width: 800px; height: 1200px; overflow: hidden; }
  body { background: var(--stage); position: relative; }

  .billboard {
    position: absolute; left: 20px; top: 410px;
    width: 760px; height: 380px;
    background: var(--paper);
    box-shadow: 0 10px 30px rgba(0,0,0,.25);
    overflow: hidden;
  }

  .park-name {
    position: absolute; left: 45px; top: 46px;
    width: 160px;
    display: flex; align-items: flex-start; gap: 8px;
  }
  .park-name__mark {
    flex: none; width: 12px; height: 12px; margin-top: 5px;
    background: var(--ink);
  }
  .park-name__text {
    font-family: "Rubik", sans-serif; font-weight: 600;
    font-size: 19px; line-height: 1.15; color: var(--ink);
    text-transform: uppercase; letter-spacing: .5px;
  }

  .headline {
    position: absolute; left: 221px; top: 17px;
    font-family: "Montserrat", sans-serif; font-weight: 900;
    font-size: 112px; line-height: 1; letter-spacing: -6px;
    color: var(--brand-red); white-space: nowrap;
  }
  .subhead {
    position: absolute; left: 330px; top: 122px;
    font-family: "Archivo Narrow", sans-serif; font-weight: 700;
    font-size: 63px; line-height: 1; color: var(--ink); white-space: nowrap;
    letter-spacing: -.5px;
    transform: scaleX(1.13); transform-origin: left top;
  }

  .directions { position: absolute; left: 25px; top: 122px; width: 296px; height: 62px; }
  .directions__text {
    position: absolute; left: 52px; top: 15px;
    font-family: "Krona One", sans-serif; font-size: 12px; line-height: 1.4;
    color: var(--paper); text-transform: uppercase; white-space: nowrap;
  }

  .info-band {
    position: absolute; left: 0; top: 193px; width: 100%; height: 187px;
    background:
      radial-gradient(ellipse at 20% 30%, var(--brand-red-light) 0%, transparent 60%),
      radial-gradient(ellipse at 85% 70%, var(--brand-red-light) 0%, transparent 55%),
      linear-gradient(180deg, var(--brand-red) 0%, var(--brand-red-deep) 100%);
  }
  .info-band__rule {
    position: absolute; left: 0; top: 145px; width: 100%; height: 1px;
    background: rgba(0,0,0,.55);
  }

  .address {
    position: absolute; left: 0; top: 17px; width: 100%;
    display: flex; justify-content: center; align-items: center; gap: 8px;
    font-family: "Rubik", sans-serif; font-weight: 600; font-size: 25px;
    color: var(--paper); white-space: nowrap;
  }
  .phone {
    position: absolute; left: 0; top: 58px; width: 100%; text-align: center;
    font-family: "Krona One", sans-serif; font-size: 60px; line-height: 1;
    color: var(--paper); letter-spacing: -2px; white-space: nowrap;
    transform: scaleX(1.2); transform-origin: center top;
  }
  .web {
    position: absolute; left: 158px; top: 130px; width: 448px; height: 30px;
    background: var(--ink); border-radius: 5px;
    display: flex; align-items: center; justify-content: center;
    font-family: "Poppins", sans-serif; font-size: 15px; letter-spacing: 2.5px;
    color: var(--paper); white-space: nowrap;
  }
  .web__prefix { font-weight: 300; }
  .web__domain { font-weight: 600; }
</style>
</head>
<body>
  <main class="billboard" aria-label="Bramblewood of Carver RV Park billboard">
    <div class="park-name">
      <span class="park-name__mark" aria-hidden="true"></span>
      <span class="park-name__text">Bramblewood of Carver RV Park</span>
    </div>

    <h1 class="headline">RV PARK</h1>

    <div class="directions">
      <svg width="296" height="62" viewBox="0 0 296 62" aria-hidden="true">
        <polygon points="0,31 36,0 36,9 296,9 296,53 36,53 36,62" fill="#111111"/>
      </svg>
      <p class="directions__text">Left on Kestrel Rd<br>then left on Danbury Rd.</p>
    </div>

    <h2 class="subhead">JUST AHEAD!</h2>

    <section class="info-band" role="img" aria-label="Deep red toned forest backdrop">
      <p class="address">
        <svg width="16" height="22" viewBox="0 0 16 22" aria-hidden="true">
          <path d="M8 0C3.6 0 0 3.5 0 7.9 0 13.5 8 22 8 22s8-8.5 8-14.1C16 3.5 12.4 0 8 0z" fill="#e4161b"/>
          <circle cx="8" cy="8" r="3.2" fill="#ffffff"/>
        </svg>
        2745 Danbury Road, Ashford Hollow , NC
      </p>
      <p class="phone">555-314-2967</p>
      <div class="info-band__rule"></div>
      <p class="web"><span class="web__prefix">www.</span><span class="web__domain">bramblewoodcarverrv</span><span class="web__prefix">.example</span></p>
    </section>
  </main>
</body>
</html>
```